Logo and business card for optometric practice
Curtis Hallorann & Associates
Marta Pelovska, O.D.
Oscar Tremwitz, O.D.
Neil Borromi, O.D.
417 Pembrook Parkway
Harrowgate Falls, Ohio 44987
555-902-4471

Target Market(s)

Patients, general public

Industry/Entity Type

Business

Logo Text

Curtis Hallorann & Associates Optometrists

Logo styles of interest
Pictorial/Combination Logo
Font styles to use
Serif
Sans Serif

Requirements
Must have
• current inspiration: realistic or photo closeup of eye, with interesting treatment of the iris OR
tech look, with closeup of eye and grid like the doctor is looking through a camera or microscope to view the eye up close
Should not have
• NO cartoons

```html
<!DOCTYPE html>
<html lang="en">
<head>
<meta charset="utf-8">
<title>Curtis Hallorann &amp; Associates — Business Card</title>
<link rel="stylesheet" href="https://fonts.googleapis.com/css2?family=Questrial&display=swap">
<style>
  :root {
    --backdrop: #ababab;
    --paper: #ffffff;
    --charcoal: #2b2b2b;
    --charcoal-light: #3a3a3a;
    --ink: #2a2a2a;
    --orange: #f7941d;
    --orange-deep: #f26522;
    --white: #ffffff;
  }
  html, body {
    margin: 0;
    padding: 0;
    width: 1200px;
    height: 900px;
    overflow: hidden;
    background: var(--backdrop);
    font-family: "Questrial", "Century Gothic", sans-serif;
  }
  .stage {
    position: relative;
    width: 1200px;
    height: 900px;
  }
  .card {
    position: absolute;
    top: 295px;
    width: 540px;
    height: 310px;
    border-radius: 24px;
    overflow: hidden;
    box-shadow: 0 10px 28px rgba(0, 0, 0, 0.28);
  }
  .card--front { left: 45px; background: var(--paper); }
  .card--back {
    left: 615px;
    background: radial-gradient(ellipse at 50% 45%, var(--charcoal-light), var(--charcoal) 75%);
  }

  .brand {
    position: absolute;
    left: 0;
    right: 0;
    display: flex;
    align-items: center;
    justify-content: center;
    gap: 12px;
    font-size: 27px;
    letter-spacing: 0.2px;
    white-space: nowrap;
  }
  .brand__dot {
    width: 14px;
    height: 14px;
    border-radius: 50%;
    background: var(--orange);
    flex: none;
  }
  .card--front .brand { top: 66px; color: var(--ink); }
  .card--back .brand { top: 134px; color: var(--white); font-size: 28px; }

  .accent-band {
    position: absolute;
    left: 0;
    right: 0;
    top: 150px;
    height: 12px;
    background: linear-gradient(90deg, var(--orange-deep), var(--orange) 60%, #fbb040);
  }
  .info-panel {
    position: absolute;
    left: 0;
    right: 0;
    top: 162px;
    bottom: 0;
    background: linear-gradient(180deg, var(--charcoal-light), var(--charcoal));
    color: var(--white);
  }
  .contact {
    position: absolute;
    left: 22px;
    top: 18px;
    font-size: 15px;
    line-height: 21px;
  }
  .contact__row {
    display: flex;
    align-items: flex-start;
    gap: 6px;
  }
  .contact__row--phone { font-size: 17px; margin-bottom: 3px; }
  .contact__icon { width: 16px; height: 16px; flex: none; margin-top: 2px; }
  .contact__lines { display: block; }
  .doctors {
    position: absolute;
    right: 34px;
    top: 16px;
    font-size: 17px;
    line-height: 25px;
    display: grid;
    grid-template-columns: auto auto;
    column-gap: 12px;
  }
  .doctors__title { color: var(--orange); }
</style>
</head>
<body>
<main class="stage">

  <section class="card card--front" aria-label="Card front">
    <div class="brand">
      <span class="brand__dot"></span>
      <span class="brand__name">Curtis Hallorann &amp; Associates</span>
    </div>
    <div class="accent-band"></div>
    <div class="info-panel">
      <div class="contact">
        <div class="contact__row contact__row--phone">
          <svg class="contact__icon" viewBox="0 0 16 16" aria-hidden="true">
            <path d="M3.2 1.2l2.4 0.1 1.1 3.1-1.6 1.3c0.8 1.8 2.1 3.1 3.9 3.9l1.3-1.6 3.1 1.1 0.1 2.4c-0.2 1.2-1.3 2-2.5 1.9C6 12.9 3.1 10 2.5 4.6 2.3 3.3 2.1 1.5 3.2 1.2z" fill="var(--orange)"/>
          </svg>
          <span>555-902-4471</span>
        </div>
        <div class="contact__row">
          <svg class="contact__icon" viewBox="0 0 16 16" aria-hidden="true">
            <path d="M8 1.5L0.8 8h2.2v6.5h3.8v-4h2.4v4h3.8V8h2.2z" fill="var(--orange)"/>
          </svg>
          <span class="contact__lines">417 Pembrook Parkway<br>Harrowgate Falls, Ohio<br>44987</span>
        </div>
      </div>
      <div class="doctors">
        <span>Marta Pelovska,</span><span class="doctors__title">O.D.</span>
        <span>Oscar Tremwitz,</span><span class="doctors__title">O.D.</span>
        <span>Neil Borromi,</span><span class="doctors__title">O.D.</span>
      </div>
    </div>
  </section>

  <section class="card card--back" aria-label="Card back">
    <div class="brand">
      <span class="brand__dot"></span>
      <span class="brand__name">Curtis Hallorann &amp; Associates</span>
    </div>
  </section>

</main>
</body>
</html>
```